Infant Massage Instructor Business Card Design

I need a business card in order to advertise my private and group parent instruction classes for massaging their infants. I am in Boulder, Colorado. I most often teach people in their own homes, but will offer group classes in other public facility venues.
I would like to use peach and lavender/ purple colors, very soft, round but clearly legible font and design. I would love to have a simple, sweeping, soft line graphic of an infant (perhaps held in adult hands?) reaching towards my business name; "Tenderly Tended Infant Massage". "Power Points" are: Reading Infant Cues, Strengthening Parent Intuition, and Nurturing Family Bonds.
"Private and group classes offered, sliding scale rates available."
THE ATTACHED LOGO IS THE LOGO OF THE "GLOBAL SOCIETY FOR BABY TOUCH", my R.B.T.P. certifying agency.

"Properly" spelled, my first name has an accent exactly over the 'e'. The top of the accent leans to the right. I would like for the name of the business to appear foremost, over my own name (which is hard for people to pronounce and 'get'). Thank you for your care and creativity in helping me promote this beautiful service offering!

I will be considering a letterhead design and postcard / brochure design as well. Please keep that in mind as you design! Thank you!

Target Market(s)

New moms and dads. Young adults to 50. Single parents, adoptive parents. Mixed economic status.

Industry/Entity Type

Adult

Contact Information for Business Card

Tenderly Tended Infant Massage
Morvel Oskin, R.B.T.P.
303-555-0182

Colors
b868aa
e667a6
a64599
f68e4e
f9bb93
f37123

Requirements
Must have
• Soft, curvy, simple line drawing of infant.
Nice to have
• Infant image, being held in adult hands
Should not have
• No "cutesy" look, please! No cartoon-like images.

```html
<!DOCTYPE html>
<html lang="en">
<head>
<meta charset="utf-8">
<title>Tenderly Tended Infant Massage – Business Card</title>
<link rel="stylesheet" href="https://fonts.googleapis.com/css2?family=Roboto+Condensed:wght@400&display=swap">
<style>
  :root {
    --canvas: #ffffff;
    --peach: #f8cc9b;
    --plum: #67286f;
    --lavender: #977db6;
    --orchid: #8a3593;
    --ink-light: #ffffff;
  }
  html, body {
    margin: 0;
    padding: 0;
    width: 1200px;
    height: 1000px;
    overflow: hidden;
    background: var(--canvas);
  }
  .canvas {
    position: relative;
    width: 1200px;
    height: 1000px;
  }
  .card {
    position: absolute;
    left: 374px;
    top: 111px;
    width: 477px;
    height: 777px;
    overflow: hidden;
    background: var(--peach);
    font-family: "Roboto Condensed", "Arial Narrow", sans-serif;
  }
  .card__art {
    position: absolute;
    inset: 0;
    width: 477px;
    height: 777px;
  }
  .business-name {
    position: absolute;
    inset: 0;
    margin: 0;
    color: var(--orchid);
    font-weight: 400;
    font-size: 42px;
    line-height: 1;
    white-space: nowrap;
  }
  .business-name__line { position: absolute; }
  .business-name__line--first { left: 117px; top: 84px; }
  .business-name__line--second { left: 48px; top: 143px; }
  .contact {
    position: absolute;
    left: 37px;
    top: 502px;
    color: var(--ink-light);
  }
  .contact__name {
    margin: 0;
    font-size: 33px;
    font-weight: 400;
    line-height: 1;
    white-space: nowrap;
  }
  .contact__phone {
    display: flex;
    align-items: center;
    gap: 10px;
    margin-top: 20px;
    font-size: 31px;
    line-height: 1;
  }
  .contact__phone-icon { width: 24px; height: 24px; fill: var(--ink-light); }
  .power-points {
    position: absolute;
    right: 37px;
    top: 645px;
    margin: 0;
    color: var(--ink-light);
    font-size: 19px;
    line-height: 28.5px;
    text-align: right;
    white-space: nowrap;
  }
</style>
</head>
<body>
<div class="canvas">
  <section class="card" aria-label="Business card">
    <svg class="card__art" viewBox="0 0 477 777">
      <defs>
        <linearGradient id="illustration-tone" x1="0" y1="0" x2="1" y2="1">
          <stop offset="0" stop-color="#977db6"/>
          <stop offset="1" stop-color="#7a4a8e"/>
        </linearGradient>
      </defs>
      <rect class="card__illustration" role="img"
        aria-label="Soft line illustration of an infant held in adult hands, reaching toward the business name"
        x="150" y="200" width="360" height="270" rx="135" fill="url(#illustration-tone)"/>
      <path class="card__band" fill="var(--plum)"
        d="M0 369 C20 352 60 342 82 372 C130 440 180 470 235 466 C330 458 420 380 477 300 L477 777 L0 777 Z"/>
      <rect class="card__faint-figure" role="img"
        aria-label="Faint outline of a parent cradling a baby"
        x="262" y="434" width="240" height="345" rx="110"
        fill="none" stroke="#8a4b90" stroke-opacity="0.45" stroke-width="6"/>
    </svg>

    <h1 class="business-name">
      <span class="business-name__line business-name__line--first">Tenderly Tended</span>
      <span class="business-name__line business-name__line--second">Infant Massage</span>
    </h1>

    <div class="contact">
      <p class="contact__name">Morvél Oskin R.B.T.P.</p>
      <div class="contact__phone">
        <svg class="contact__phone-icon" viewBox="0 0 24 24" aria-hidden="true">
          <path d="M6.6 10.8c1.4 2.8 3.8 5.1 6.6 6.6l2.2-2.2c.3-.3.7-.4 1-.2 1.1.4 2.3.6 3.6.6.6 0 1 .4 1 1V20c0 .6-.4 1-1 1C10.6 21 3 13.4 3 4c0-.6.4-1 1-1h3.5c.6 0 1 .4 1 1 0 1.3.2 2.5.6 3.6.1.3 0 .7-.2 1l-2.3 2.2z"/>
        </svg>
        <span class="contact__phone-number">303-555-0182</span>
      </div>
    </div>

    <p class="power-points">Reading Infant Cues,<br>Strengthening Parent Intuition<br>and Nurturing Family Bonds.</p>
  </section>
</div>
</body>
</html>
```